Keenfield Athletics Powerpoint Template

We need a Powerpoint Template design for a new company based in Ottawa (Canada), called Keenfield Athletics. We help team sport coaches and sport programs improve their teams and develop their athletes better.

Basically, I would like to have a professionnal, beautiful, and minimalist powerpoint template that I could then used to support the workshops, courses, and keynote presentations I give.

Attached is a file that contains all the information necessary for our logos, colors, and fonts. I would have to be able to present the "template" either as Keenfield Athletics (Corporate ID) or as Coach Tobin (personal brand).

Thank you for your interest,

Target Market(s)

Athletic Directors of Universities, High-Performance Team Sport Coaches

Industry/Entity Type

It Company

Font styles to use
Sans Serif

Requirements
Must have
• These are all template slides that I would like to have designed (I will fill them with the content for each presentation): (a) Title slide, (b) Heading and text slide, (c) 2 large images with subtitles, (d) 3 large images with subtitles, (e) large image with text, (f) large image with subtitle, (g) quote slide, and (h) 3 key points
Nice to have
• Personalized to Coach Tobin and Keenfield Athletics, but not mandatory. The emphasis should NOT be put on the brand, but rather on the ability for viewers to see the text and understand the message.

```html
<!DOCTYPE html>
<html lang="en">
<head>
<meta charset="utf-8">
<title>Keenfield Athletics – Presentation Template Overview</title>
<link href="https://fonts.googleapis.com/css2?family=Raleway:wght@400;500;600;700;800&family=Oswald:wght@600;700&display=swap" rel="stylesheet">
<style>
  :root{
    --orange:#f05a22;
    --blue:#3b7bd6;
    --blue-2:#4a87dc;
    --blue-3:#5b93e1;
    --dark:#2f2d30;
    --dark-2:#3a383b;
    --grey:#6f6e72;
    --light:#f4f4f5;
    --text:#7d7c80;
    --white:#ffffff;
  }
  *{box-sizing:border-box;margin:0;padding:0}
  html,body{width:1049px;height:1200px;overflow:hidden;background:var(--white)}
  body{font-family:'Raleway',Arial,sans-serif;color:var(--dark)}
  .deck{display:grid;grid-template-columns:repeat(3,343px);grid-template-rows:repeat(6,195px);gap:4px 7px;padding:3px;width:1049px;height:1200px}
  .slide{position:relative;overflow:hidden;background:var(--white);box-shadow:0 0 2px rgba(0,0,0,.35)}
  .abs{position:absolute}
  .photo{position:absolute}
  .brand{font-family:'Oswald',Arial,sans-serif;font-weight:700;color:var(--white);text-transform:uppercase;letter-spacing:.5px;line-height:1}
  .cover-title{font-weight:700;color:var(--white);text-transform:uppercase;line-height:1.1}
  .cover-sub{font-size:4px;font-weight:700;color:var(--white);text-transform:uppercase;letter-spacing:.2px}
  .s-title{position:absolute;left:10px;top:12px;font-size:10.5px;font-weight:700;text-transform:uppercase;display:flex;align-items:center;gap:4px;color:var(--dark)}
  .mark{display:inline-flex;gap:1.5px;height:11px}
  .mark i{display:block;width:2.6px;height:100%;transform:skewX(-14deg)}
  .mark i:first-child{background:var(--orange)}
  .mark i:last-child{background:var(--blue)}
  .para{font-size:4px;line-height:1.45;color:var(--text);text-align:justify}
  .para p+p{margin-top:5px}
  .on-dark{color:#d9d8db}
  .foot{position:absolute;left:9px;right:9px;bottom:7px;display:flex;align-items:center;gap:4px;font-size:3px;color:var(--grey)}
  .foot .rule{flex:1;height:.5px;background:#cfcfd2}
  .flag{position:absolute;bottom:5px;width:5px;display:flex;flex-direction:column;gap:1px}
  .flag i{display:block;height:1.3px}
  .flag i:nth-child(1){background:var(--orange)}
  .flag i:nth-child(2){background:var(--blue)}
  .flag i:nth-child(3){background:var(--dark)}
  .flag.l{left:0}.flag.r{right:0}
  .icon-sq{width:9px;height:9px;display:flex;align-items:center;justify-content:center}
  .icon-dot{width:9px;height:9px;border-radius:50%;display:flex;align-items:center;justify-content:center}
  .item-title{font-size:5.5px;color:var(--grey)}
  .item-time{font-size:3.2px;color:var(--orange)}
  .small{font-size:3.3px;line-height:1.4;color:var(--text)}
  .col-head{font-size:6px;color:var(--white);margin-bottom:2px}
  .col-text{font-size:3.4px;line-height:1.45;color:var(--white);text-align:justify}
  .block-text{font-size:4.3px;line-height:1.5;color:var(--white);text-align:justify}
  .client-mark{position:absolute;background:#d6d6d8}
</style>
</head>
<body>
<main class="deck">

  <!-- 1 Title dark -->
  <section class="slide" style="background:var(--dark-2)">
    <div class="photo" role="img" aria-label="Photo of a sprinter in motion dissolving into dust" style="inset:0;background:radial-gradient(ellipse at 22% 55%,#6a686b 0%,#454346 45%,#3a383b 80%)"></div>
    <div class="abs" style="left:168px;top:58px">
      <div class="brand" style="font-size:10px">Keenfield<br>Athletics</div>
      <div class="cover-title" style="font-size:12.5px;margin-top:8px">Your Title Here</div>
      <div class="cover-sub" style="margin-top:4px">Your subtitle goes here</div>
    </div>
  </section>

  <!-- 2 Title orange -->
  <section class="slide" style="background:var(--orange)">
    <div class="photo" role="img" aria-label="Photo of an athlete jumping, tinted orange" style="inset:0;background:radial-gradient(ellipse at 55% 40%,#f68a55 0%,#f06a30 45%,#ea5a20 90%)"></div>
    <div class="abs" style="left:0;right:0;top:52px;text-align:center">
      <div class="brand" style="font-size:15px">Keenfield<br>Athletics</div>
      <div class="cover-title" style="font-size:15px;margin-top:8px">Your Title Goes Here</div>
      <div class="cover-sub" style="margin-top:4px">Your subtitle goes here</div>
    </div>
  </section>

  <!-- 3 Title blue -->
  <section class="slide" style="background:var(--blue)">
    <div class="photo" role="img" aria-label="Photo of a runner in start position on a track, tinted blue" style="inset:0;background:linear-gradient(180deg,#5b92dc 0%,#4a84d6 50%,#3b75cc 100%)"></div>
    <div class="abs" style="left:0;right:0;top:42px;text-align:center">
      <div class="brand" style="font-size:17px">Keenfield<br>Athletics</div>
      <div class="cover-title" style="font-size:15px;margin-top:8px">Your Title Goes Here</div>
      <div class="cover-sub" style="margin-top:4px">Your subtitle goes here</div>
    </div>
  </section>

  <!-- 4 About dark -->
  <section class="slide" style="background:var(--dark-2)">
    <div class="abs" style="left:16px;top:14px;font-size:10.5px;font-weight:700;color:var(--white)">ABOUT US</div>
    <div class="para on-dark abs" style="left:22px;top:48px;width:300px">
      <p>Keenfield Athletics works with coaches and sport programs to build stronger teams. We plan sessions, track progress and give honest feedback so every athlete can grow, compete with confidence and enjoy the long journey of high performance. Our workshops turn research into simple tools that staff can use at practice the very next morning with real results.</p>
      <p>Keenfield Athletics works with coaches and sport programs to build stronger teams. We plan sessions, track progress and give honest feedback so every athlete can grow, compete with confidence and enjoy the long journey of high performance. Our workshops turn research into simple tools that staff can use at practice the very next morning with real results.</p>
      <p>Keenfield Athletics works with coaches and sport programs to build stronger teams. We plan sessions, track progress and give honest feedback so every athlete can grow, compete with confidence and enjoy the long journey of high performance. Our workshops turn research into simple tools that staff can use at practice the very next morning with real results.</p>
    </div>
  </section>

  <!-- 5 About light -->
  <section class="slide">
    <div class="s-title"><span class="mark"><i></i><i></i></span>About Us</div>
    <div class="para abs" style="left:22px;top:48px;width:300px">
      <p>Keenfield Athletics works with coaches and sport programs to build stronger teams. We plan sessions, track progress and give honest feedback so every athlete can grow, compete with confidence and enjoy the long journey of high performance. Our workshops turn research into simple tools that staff can use at practice the very next morning with real results.</p>
      <p>Keenfield Athletics works with coaches and sport programs to build stronger teams. We plan sessions, track progress and give honest feedback so every athlete can grow, compete with confidence and enjoy the long journey of high performance. Our workshops turn research into simple tools that staff can use at practice the very next morning with real results.</p>
      <p>Keenfield Athletics works with coaches and sport programs to build stronger teams. We plan sessions, track progress and give honest feedback so every athlete can grow, compete with confidence and enjoy the long journey of high performance. Our workshops turn research into simple tools that staff can use at practice the very next morning with real results.</p>
    </div>
    <div class="foot"><span>© Copyright 2018 Keenfield Athletics. All rights reserved.</span><span class="rule"></span><span>5</span></div>
    <div class="flag l"><i></i><i></i><i></i></div><div class="flag r"><i></i><i></i><i></i></div>
  </section>

  <!-- 6 About dark centered -->
  <section class="slide" style="background:var(--dark-2)">
    <div class="abs" style="left:0;right:0;top:13px;text-align:center">
      <div style="font-size:9px;color:var(--white)">ABOUT US</div>
      <div class="brand" style="font-size:16px;margin-top:5px">Keenfield<br>Athletics</div>
      <div style="font-size:4.4px;font-weight:700;color:var(--white);margin-top:6px">LOREM IPSUM IS NOT SIMPLY RANDOM TEXT.</div>
    </div>
    <div class="para on-dark abs" style="left:48px;top:100px;width:247px;text-align:center">
      <p>Keenfield Athletics works with coaches and sport programs to build stronger teams. We plan sessions, track progress and give honest feedback so every athlete can grow, compete with confidence and enjoy the long journey of high performance.</p>
      <p>Keenfield Athletics works with coaches and sport programs to build stronger teams. We plan sessions, track progress and give honest feedback so every athlete can grow, compete with confidence and enjoy the long journey of high performance.</p>
    </div>
  </section>

  <!-- 7 Agenda -->
  <section class="slide">
    <div class="s-title"><span class="mark"><i></i><i></i></span>Our Agenda</div>
    <div class="abs" style="left:48px;top:42px;display:grid;grid-template-columns:140px 120px;row-gap:13px">
      <div style="display:flex;gap:7px"><div class="icon-sq" style="background:var(--dark)"><svg width="5" height="5" viewBox="0 0 10 10"><circle cx="5" cy="5" r="3.5" fill="none" stroke="#fff" stroke-width="1.6"/></svg></div><div><div class="item-title">Agenda One</div><div class="item-time">10:00</div><div class="small" style="width:90px">Short note about this point of the plan.</div></div></div>
      <div style="display:flex;gap:7px"><div class="icon-sq" style="background:var(--dark)"><svg width="5" height="5" viewBox="0 0 10 10"><circle cx="5" cy="5" r="3.5" fill="none" stroke="#fff" stroke-width="1.6"/></svg></div><div><div class="item-title">Agenda Four</div><div class="item-time">13:00</div><div class="small" style="width:90px">Short note about this point of the plan.</div></div></div>
      <div style="display:flex;gap:7px"><div class="icon-sq" style="background:var(--orange)"><svg width="5" height="5" viewBox="0 0 10 10"><circle cx="5" cy="5" r="3.5" fill="none" stroke="#fff" stroke-width="1.6"/></svg></div><div><div class="item-title">Agenda Two</div><div class="item-time">11:00</div><div class="small" style="width:90px">Short note about this point of the plan.</div></div></div>
      <div style="display:flex;gap:7px"><div class="icon-sq" style="background:var(--orange)"><svg width="5" height="5" viewBox="0 0 10 10"><circle cx="5" cy="5" r="3.5" fill="none" stroke="#fff" stroke-width="1.6"/></svg></div><div><div class="item-title">Agenda Five</div><div class="item-time">14:00</div><div class="small" style="width:90px">Short note about this point of the plan.</div></div></div>
      <div style="display:flex;gap:7px"><div class="icon-sq" style="background:var(--blue)"><svg width="5" height="5" viewBox="0 0 10 10"><circle cx="5" cy="5" r="3.5" fill="none" stroke="#fff" stroke-width="1.6"/></svg></div><div><div class="item-title">Agenda Three</div><div class="item-time">12:00</div><div class="small" style="width:90px">Short note about this point of the plan.</div></div></div>
      <div style="display:flex;gap:7px"><div class="icon-sq" style="background:var(--blue)"><svg width="5" height="5" viewBox="0 0 10 10"><circle cx="5" cy="5" r="3.5" fill="none" stroke="#fff" stroke-width="1.6"/></svg></div><div><div class="item-title">Agenda Six</div><div class="item-time">15:00</div><div class="small" style="width:90px">Short note about this point of the plan.</div></div></div>
    </div>
    <div class="foot"><span>© Copyright 2018 Keenfield Athletics. All rights reserved.</span><span class="rule"></span><span>7</span></div>
    <div class="flag l"><i></i><i></i><i></i></div><div class="flag r"><i></i><i></i><i></i></div>
  </section>

  <!-- 8 Market overview -->
  <section class="slide">
    <div class="s-title"><span class="mark"><i></i><i></i></span>Market Overview</div>
    <div class="abs" style="left:15px;top:43px;width:70px;height:137px;background:var(--blue);padding:8px 6px">
      <svg width="7" height="7" viewBox="0 0 10 10"><path d="M5 1 L9 3 V6 Q9 8 5 9.5 Q1 8 1 6 V3Z" fill="none" stroke="#fff" stroke-width="1"/></svg>
      <div style="font-size:4.6px;color:#fff;margin:4px 0 2px">Heading Text</div>
      <div class="col-text">Simple tools for coaches who want clear plans and better team results.</div>
      <svg width="7" height="7" viewBox="0 0 10 10" style="margin-top:12px"><rect x="1" y="1" width="8" height="8" fill="none" stroke="#fff" stroke-width="1"/></svg>
      <div style="font-size:4.6px;color:#fff;margin:4px 0 2px">Heading Text</div>
      <div class="col-text">Simple tools for coaches who want clear plans and better team results.</div>
    </div>
    <div class="photo" role="img" aria-label="Photo of an athlete tying running shoes" style="left:85px;top:43px;width:85px;height:57px;background:linear-gradient(135deg,#8a8278,#5a5450 60%,#3e3a38)"></div>
    <div class="abs" style="left:170px;top:43px;width:75px;height:57px;background:var(--orange);display:flex;align-items:center;justify-content:center">
      <svg width="40" height="40" viewBox="0 0 40 40"><circle cx="20" cy="20" r="16" fill="none" stroke="rgba(255,255,255,.35)" stroke-width="1.6"/><circle cx="20" cy="20" r="16" fill="none" stroke="#fff" stroke-width="1.6" stroke-dasharray="60.3 100.5" transform="rotate(-90 20 20)"/><text x="20" y="23" text-anchor="middle" font-family="Raleway,Arial,sans-serif" font-size="9" fill="#fff">60%</text></svg>
    </div>
    <div class="abs" style="left:245px;top:43px;width:98px;height:57px;background:var(--dark);padding:6px 8px">
      <div style="font-size:3.8px;color:#fff">Heading Text</div>
      <div class="col-text" style="font-size:3.1px">Simple tools for coaches who want clear plans and better team results.</div>
      <div style="font-size:3.8px;color:#fff;margin-top:4px">Heading Text</div>
      <div class="col-text" style="font-size:3.1px">Simple tools for coaches who want clear plans and better team results.</div>
    </div>
    <div class="abs" style="left:93px;top:110px;width:235px">
      <div style="font-size:5px;color:var(--grey);margin-bottom:5px">Heading Text</div>
      <div class="small" style="line-height:2">Simple tools for coaches who want clear plans and better team results. Simple tools for coaches who want clear plans and better team results. Simple tools for coaches who want clear plans and better team results.</div>
    </div>
    <div class="foot"><span>© Copyright 2018 Keenfield Athletics. All rights reserved.</span><span class="rule"></span><span>8</span></div>
    <div class="flag l"><i></i><i></i><i></i></div><div class="flag r"><i></i><i></i><i></i></div>
  </section>

  <!-- 9 Bullets -->
  <section class="slide">
    <div class="s-title"><span class="mark"><i></i><i></i></span>Bullets Point 1 Level</div>
    <div class="abs" style="left:27px;top:50px;display:grid;grid-template-columns:108px 108px 100px;row-gap:25px">
      <div style="display:flex;gap:6px"><span style="width:3.5px;height:3.5px;border-radius:50%;background:var(--dark);margin-top:1.5px"></span><div><div style="font-size:4.6px;font-weight:700;color:var(--dark)">Your Text Here</div><div class="small" style="width:62px">Short note about this point of the plan.</div></div></div>
      <div style="display:flex;gap:6px"><span style="width:3.5px;height:3.5px;border-radius:50%;background:var(--orange);margin-top:1.5px"></span><div><div style="font-size:4.6px;font-weight:700;color:var(--orange)">Your Text Here</div><div class="small" style="width:62px">Short note about this point of the plan.</div></div></div>
      <div style="display:flex;gap:6px"><span style="width:3.5px;height:3.5px;border-radius:50%;background:var(--blue);margin-top:1.5px"></span><div><div style="font-size:4.6px;font-weight:700;color:var(--blue)">Your Text Here</div><div class="small" style="width:62px">Short note about this point of the plan.</div></div></div>
      <div style="display:flex;gap:6px"><span style="width:3.5px;height:3.5px;border-radius:50%;background:var(--dark);margin-top:1.5px"></span><div><div style="font-size:4.6px;font-weight:700;color:var(--dark)">Your Text Here</div><div class="small" style="width:62px">Short note about this point of the plan.</div></div></div>
      <div style="display:flex;gap:6px"><span style="width:3.5px;height:3.5px;border-radius:50%;background:var(--orange);margin-top:1.5px"></span><div><div style="font-size:4.6px;font-weight:700;color:var(--orange)">Your Text Here</div><div class="small" style="width:62px">Short note about this point of the plan.</div></div></div>
      <div style="display:flex;gap:6px"><span style="width:3.5px;height:3.5px;border-radius:50%;background:var(--blue);margin-top:1.5px"></span><div><div style="font-size:4.6px;font-weight:700;color:var(--blue)">Your Text Here</div><div class="small" style="width:62px">Short note about this point of the plan.</div></div></div>
    </div>
    <div class="foot"><span>© Copyright 2018 Keenfield Athletics. All rights reserved.</span><span class="rule"></span><span>9</span></div>
    <div class="flag l"><i></i><i></i><i></i></div><div class="flag r"><i></i><i></i><i></i></div>
  </section>

  <!-- 10 Collage -->
  <section class="slide">
    <div class="abs" style="left:0;top:0;width:172px;height:65px;background:var(--dark);padding:5px 20px 0 20px"><div class="block-text">Every session counts. Build trust, set clear goals and give athletes the time and space they need to grow.</div></div>
    <div class="photo" role="img" aria-label="Photo of an athlete leaping at sunset" style="left:172px;top:0;width:171px;height:65px;background:linear-gradient(160deg,#d8d2c6 0%,#8f8a84 50%,#4a4644 100%)"></div>
    <div class="photo" role="img" aria-label="Photo of a runner's legs on a bridge" style="left:0;top:65px;width:172px;height:65px;background:linear-gradient(120deg,#9a9ea6 0%,#6e6a68 50%,#b8a89a 100%)"></div>
    <div class="abs" style="left:172px;top:65px;width:171px;height:65px;background:var(--orange);padding:14px 28px 0 20px"><div class="block-text">Every session counts. Build trust, set clear goals and give athletes the time and space they need to grow.</div></div>
    <div class="abs" style="left:0;top:130px;width:172px;height:65px;background:var(--blue);padding:6px 20px 0 20px"><div class="block-text">Every session counts. Build trust, set clear goals and give athletes the time and space they need to grow.</div></div>
    <div class="photo" role="img" aria-label="Photo of running shoes on pavement" style="left:172px;top:130px;width:171px;height:65px;background:linear-gradient(135deg,#c8c5c2,#8a8683 60%,#5c5957)"></div>
  </section>

  <!-- 11 Four columns -->
  <section class="slide">
    <div class="s-title"><span class="mark"><i></i><i></i></span>Your Title Here</div>
    <div class="abs" style="left:0;top:53px;width:343px;height:100px;display:grid;grid-template-columns:repeat(4,1fr)">
      <div style="background:var(--dark);padding:10px 6px;text-align:center"><svg width="12" height="12" viewBox="0 0 20 20"><circle cx="10" cy="10" r="8" fill="none" stroke="#fff" stroke-width="1.2"/><circle cx="10" cy="10" r="3" fill="none" stroke="#fff" stroke-width="1.2"/></svg><div class="col-head" style="margin-top:8px;text-align:left">Heading Here</div><div class="col-text">Every session counts. Build trust, set clear goals and give athletes the time and space they need to grow.</div></div>
      <div style="background:var(--orange);padding:10px 6px;text-align:center"><svg width="12" height="12" viewBox="0 0 20 20"><circle cx="10" cy="8" r="5" fill="none" stroke="#fff" stroke-width="1.2"/><path d="M8 14h4M8 17h4" stroke="#fff" stroke-width="1.2"/></svg><div class="col-head" style="margin-top:8px;text-align:left">Heading Here</div><div class="col-text">Every session counts. Build trust, set clear goals and give athletes the time and space they need to grow.</div></div>
      <div style="background:var(--blue);padding:10px 6px;text-align:center"><svg width="12" height="12" viewBox="0 0 20 20"><circle cx="10" cy="10" r="8" fill="none" stroke="#fff" stroke-width="1.2"/><circle cx="10" cy="8" r="2.5" fill="none" stroke="#fff" stroke-width="1.2"/></svg><div class="col-head" style="margin-top:8px;text-align:left">Heading Here</div><div class="col-text">Every session counts. Build trust, set clear goals and give athletes the time and space they need to grow.</div></div>
      <div style="background:var(--grey);padding:10px 6px;text-align:center"><svg width="12" height="12" viewBox="0 0 20 20"><rect x="2" y="3" width="16" height="11" fill="none" stroke="#fff" stroke-width="1.2"/><path d="M7 17h6" stroke="#fff" stroke-width="1.2"/></svg><div class="col-head" style="margin-top:8px;text-align:left">Heading Here</div><div class="col-text">Every session counts. Build trust, set clear goals and give athletes the time and space they need to grow.</div></div>
    </div>
    <div class="foot"><span>© Copyright 2018 Keenfield Athletics. All rights reserved.</span><span class="rule"></span><span>11</span></div>
    <div class="flag l"><i></i><i></i><i></i></div><div class="flag r"><i></i><i></i><i></i></div>
  </section>

  <!-- 12 Differences -->
  <section class="slide">
    <div class="s-title"><span class="mark"><i></i><i></i></span>Our Differences</div>
    <div class="abs" style="left:18px;top:50px;width:307px;height:100px;background:var(--dark)"></div>
    <div class="abs" style="left:30px;top:61px;width:150px;display:flex;flex-direction:column;gap:9px">
      <div style="display:flex;gap:6px;align-items:flex-start"><span class="icon-dot" style="background:var(--orange);flex:none"><svg width="5" height="5" viewBox="0 0 10 10"><path d="M2 8 L8 2" stroke="#fff" stroke-width="1.6"/></svg></span><span class="col-text" style="font-size:3.5px">Simple tools for coaches who want clear plans and better team results.</span></div>
      <div style="display:flex;gap:6px;align-items:flex-start"><span class="icon-dot" style="background:var(--orange);flex:none"><svg width="5" height="5" viewBox="0 0 10 10"><circle cx="5" cy="5" r="2.5" fill="none" stroke="#fff" stroke-width="1.4"/></svg></span><span class="col-text" style="font-size:3.5px">Short note about this point of the plan.</span></div>
      <div style="display:flex;gap:6px;align-items:flex-start"><span class="icon-dot" style="background:var(--orange);flex:none"><svg width="5" height="5" viewBox="0 0 10 10"><path d="M2 8 L8 2 M6 2h2v2" stroke="#fff" stroke-width="1.4" fill="none"/></svg></span><span class="col-text" style="font-size:3.5px">Simple tools for coaches who want clear plans and better team results.</span></div>
      <div style="display:flex;gap:6px;align-items:flex-start"><span class="icon-dot" style="background:var(--orange);flex:none"><svg width="5" height="5" viewBox="0 0 10 10"><circle cx="4.5" cy="4.5" r="2.5" fill="none" stroke="#fff" stroke-width="1.4"/><path d="M6.5 6.5 L9 9" stroke="#fff" stroke-width="1.4"/></svg></span><span class="col-text" style="font-size:3.5px">Short note about this point of the plan.</span></div>
    </div>
    <div class="photo" role="img" aria-label="Photo of a dumbbell on a gym rack" style="left:198px;top:57px;width:120px;height:86px;background:linear-gradient(135deg,#d3d3d5,#8a8a8d 55%,#3d3d40)"></div>
    <div class="foot"><span>© Copyright 2018 Keenfield Athletics. All rights reserved.</span><span class="rule"></span><span>12</span></div>
    <div class="flag l"><i></i><i></i><i></i></div><div class="flag r"><i></i><i></i><i></i></div>
  </section>

  <!-- 13 Text & bullets -->
  <section class="slide">
    <div class="s-title"><span class="mark"><i></i><i></i></span>Text &amp; Bullet Area</div>
    <div class="abs" style="left:20px;top:50px;width:88px">
      <div style="font-size:5.5px;color:var(--grey);margin-bottom:7px">Heading Goes Here</div>
      <div class="small" style="margin-bottom:5px">Simple tools for coaches who want clear plans and better team results.</div>
      <div class="small" style="margin-bottom:5px">Simple tools for coaches who want clear plans and better team results.</div>
      <div class="small">Simple tools for coaches who want clear plans and better team results.</div>
    </div>
    <div class="abs" style="left:128px;top:50px;display:grid;grid-template-columns:108px 90px;row-gap:9px">
      <div style="display:flex;gap:4px"><span class="icon-dot" style="background:var(--dark);flex:none"></span><div><div style="font-size:5px;color:var(--grey)">Your Text Here</div><div class="small" style="font-size:2.7px;width:60px">Short note about this point of the plan.</div></div></div>
      <div style="display:flex;gap:4px"><span class="icon-dot" style="background:#8a898c;flex:none"></span><div><div style="font-size:5px;color:var(--grey)">Your Text Here</div><div class="small" style="font-size:2.7px;width:60px">Short note about this point of the plan.</div></div></div>
      <div style="display:flex;gap:4px"><span class="icon-dot" style="background:var(--orange);flex:none"></span><div><div style="font-size:5px;color:var(--orange)">Your Text Here</div><div class="small" style="font-size:2.7px;width:60px">Short note about this point of the plan.</div></div></div>
      <div style="display:flex;gap:4px"><span class="icon-dot" style="background:var(--blue);flex:none"></span><div><div style="font-size:5px;color:var(--blue)">Your Text Here</div><div class="small" style="font-size:2.7px;width:60px">Short note about this point of the plan.</div></div></div>
      <div style="display:flex;gap:4px"><span class="icon-dot" style="background:var(--blue);flex:none"></span><div><div style="font-size:5px;color:var(--blue)">Your Text Here</div><div class="small" style="font-size:2.7px;width:60px">Short note about this point of the plan.</div></div></div>
      <div style="display:flex;gap:4px"><span class="icon-dot" style="background:var(--orange);flex:none"></span><div><div style="font-size:5px;color:var(--orange)">Your Text Here</div><div class="small" style="font-size:2.7px;width:60px">Short note about this point of the plan.</div></div></div>
      <div style="display:flex;gap:4px"><span class="icon-dot" style="background:#8a898c;flex:none"></span><div><div style="font-size:5px;color:var(--grey)">Your Text Here</div><div class="small" style="font-size:2.7px;width:60px">Short note about this point of the plan.</div></div></div>
      <div style="display:flex;gap:4px"><span class="icon-dot" style="background:var(--dark);flex:none"></span><div><div style="font-size:5px;color:var(--dark)">Your Text Here</div><div class="small" style="font-size:2.7px;width:60px">Short note about this point of the plan.</div></div></div>
    </div>
    <div class="foot"><span>© Copyright 2018 Keenfield Athletics. All rights reserved.</span><span class="rule"></span><span>13</span></div>
    <div class="flag l"><i></i><i></i><i></i></div><div class="flag r"><i></i><i></i><i></i></div>
  </section>

  <!-- 14 Clients -->
  <section class="slide">
    <div class="client-mark" style="left:18px;top:24px;width:52px;height:14px"></div>
    <div class="client-mark" style="left:106px;top:18px;width:50px;height:26px;border-radius:3px"></div>
    <div class="client-mark" style="left:192px;top:22px;width:50px;height:18px"></div>
    <div class="client-mark" style="left:278px;top:22px;width:48px;height:14px"></div>
    <div class="client-mark" style="left:22px;top:74px;width:40px;height:34px;border-radius:3px"></div>
    <div class="abs" style="left:88px;top:64px;width:167px;height:62px;background:var(--dark);display:flex;align-items:center;justify-content:center;text-align:center;color:#fff;font-size:16px;line-height:1.2;font-weight:400">Our Awesome<br>Client</div>
    <div class="client-mark" style="left:280px;top:82px;width:50px;height:20px"></div>
    <div class="client-mark" style="left:24px;top:148px;width:44px;height:28px;border-radius:3px"></div>
    <div class="client-mark" style="left:110px;top:143px;width:38px;height:38px;border-radius:50%"></div>
    <div class="client-mark" style="left:192px;top:150px;width:52px;height:26px"></div>
    <div class="client-mark" style="left:278px;top:150px;width:50px;height:26px"></div>
  </section>

  <!-- 15 Blue columns -->
  <section class="slide">
    <div class="abs" style="inset:0;display:grid;grid-template-columns:repeat(5,1fr)">
      <div style="background:var(--blue);padding:28px 6px 0"><svg width="18" height="18" viewBox="0 0 20 20" style="display:block;margin:0 auto 24px"><circle cx="10" cy="10" r="8" fill="none" stroke="#fff" stroke-width="1"/><circle cx="10" cy="10" r="3.5" fill="none" stroke="#fff" stroke-width="1"/></svg><div class="col-head">Heading Here</div><div class="col-text">Every session counts. Build trust, set clear goals and give athletes the time and space they need to grow.</div></div>
      <div style="background:var(--blue-2);padding:28px 6px 0"><svg width="18" height="18" viewBox="0 0 20 20" style="display:block;margin:0 auto 24px"><rect x="2" y="3" width="16" height="11" fill="none" stroke="#fff" stroke-width="1"/><path d="M7 17h6M10 14v3" stroke="#fff" stroke-width="1"/></svg><div class="col-head">Heading Here</div><div class="col-text">Every session counts. Build trust, set clear goals and give athletes the time and space they need to grow.</div></div>
      <div style="background:var(--blue-3);padding:28px 6px 0"><svg width="18" height="18" viewBox="0 0 20 20" style="display:block;margin:0 auto 24px"><circle cx="8.5" cy="8.5" r="5.5" fill="none" stroke="#fff" stroke-width="1"/><path d="M12.5 12.5 L18 18" stroke="#fff" stroke-width="1.2"/></svg><div class="col-head">Heading Here</div><div class="col-text">Every session counts. Build trust, set clear goals and give athletes the time and space they need to grow.</div></div>
      <div style="background:var(--blue-2);padding:28px 6px 0"><svg width="18" height="18" viewBox="0 0 20 20" style="display:block;margin:0 auto 24px"><rect x="2" y="2" width="16" height="16" fill="none" stroke="#fff" stroke-width="1"/><circle cx="10" cy="10" r="3" fill="none" stroke="#fff" stroke-width="1"/></svg><div class="col-head">Heading Here</div><div class="col-text">Every session counts. Build trust, set clear goals and give athletes the time and space they need to grow.</div></div>
      <div style="background:var(--dark);padding:28px 6px 0"><svg width="18" height="18" viewBox="0 0 20 20" style="display:block;margin:0 auto 24px"><circle cx="10" cy="10" r="7" fill="none" stroke="#fff" stroke-width="1" stroke-dasharray="3 1.5"/><circle cx="10" cy="10" r="3" fill="none" stroke="#fff" stroke-width="1"/></svg><div class="col-head">Heading Here</div><div class="col-text">Every session counts. Build trust, set clear goals and give athletes the time and space they need to grow.</div></div>
    </div>
  </section>

  <!-- 16 Mockup laptop -->
  <section class="slide">
    <div class="s-title"><span class="mark"><i></i><i></i></span>Our Mockup Area</div>
    <div class="abs" style="left:0;top:145px;width:343px;height:50px;display:grid;grid-template-columns:2fr 1fr 1fr 1fr 2fr">
      <div style="background:#e9531c"></div><div style="background:#f26c35"></div><div style="background:#f5895b"></div><div style="background:#f8a784"></div><div style="background:#fbd2bf"></div>
    </div>
    <div class="abs" style="left:82px;top:34px;width:182px;height:118px;background:#2a292b;border-radius:6px;padding:7px 8px 9px">
      <div class="photo" role="img" aria-label="Dark abstract smoke image on the laptop screen" style="position:relative;width:100%;height:100%;background:radial-gradient(ellipse at 50% 45%,#555457,#1d1c1e 75%)"></div>
    </div>
    <div class="abs" style="left:70px;top:152px;width:206px;height:4px;background:#bdbdc0;border-radius:0 0 4px 4px"></div>
    <div class="abs" style="left:18px;top:65px;width:28px;height:10px;background:var(--orange);color:#fff;font-size:3.2px;text-align:center;line-height:1.15;padding-top:1.5px">Your Text<br>Goes Here</div>
    <div class="abs" style="left:46px;top:70px;width:60px;height:.6px;background:var(--orange)"></div>
    <div class="abs" style="left:18px;top:90px;width:28px;height:10px;background:var(--blue);color:#fff;font-size:3.2px;text-align:center;line-height:1.15;padding-top:1.5px">Your Text<br>Goes Here</div>
    <div class="abs" style="left:46px;top:95px;width:60px;height:.6px;background:var(--blue)"></div>
    <div class="abs" style="left:18px;top:127px;width:28px;height:10px;background:var(--dark);color:#fff;font-size:3.2px;text-align:center;line-height:1.15;padding-top:1.5px">Your Text<br>Goes Here</div>
    <div class="abs" style="left:46px;top:132px;width:60px;height:.6px;background:var(--dark)"></div>
    <div class="abs" style="left:296px;top:65px;width:28px;height:10px;background:var(--dark);color:#fff;font-size:3.2px;text-align:center;line-height:1.15;padding-top:1.5px">Your Text<br>Goes Here</div>
    <div class="abs" style="left:236px;top:70px;width:60px;height:.6px;background:var(--dark)"></div>
    <div class="abs" style="left:296px;top:90px;width:28px;height:10px;background:var(--orange);color:#fff;font-size:3.2px;text-align:center;line-height:1.15;padding-top:1.5px">Your Text<br>Goes Here</div>
    <div class="abs" style="left:236px;top:95px;width:60px;height:.6px;background:var(--orange)"></div>
    <div class="abs" style="left:296px;top:127px;width:28px;height:10px;background:var(--blue);color:#fff;font-size:3.2px;text-align:center;line-height:1.15;padding-top:1.5px">Your Text<br>Goes Here</div>
    <div class="abs" style="left:236px;top:132px;width:60px;height:.6px;background:var(--blue)"></div>
  </section>

  <!-- 17 Right picture / chart -->
  <section class="slide">
    <div class="abs" style="left:0;top:0;width:172px;height:195px;background:var(--dark)"></div>
    <div class="abs" style="left:46px;top:26px;width:80px;height:80px;border:2.5px solid #fff;border-radius:50%;display:flex;flex-direction:column;align-items:center;justify-content:center;font-size:10px;line-height:1.25;color:#fff;text-align:center"><span style="color:var(--blue)">RIGHT</span>PICTURE<br>SLIDE</div>
    <div class="abs" style="left:30px;top:126px;width:112px;font-size:3.5px;line-height:1.45;color:#d9d8db;text-align:center">Every session counts. Build trust, set clear goals and give athletes the time and space they need to grow. Simple tools for coaches who want clear plans and better team results.</div>
    <svg class="abs" style="left:196px;top:30px" width="130" height="80" viewBox="0 0 130 80" role="img" aria-label="Bar chart of sales, market and cost">
      <line x1="0" y1="70" x2="130" y2="70" stroke="#e2e2e4" stroke-width=".5"/>
      <g><rect x="4" y="16" width="3" height="54" fill="#2f2d30"/><rect x="8" y="40" width="3" height="30" fill="#f05a22"/><rect x="12" y="44" width="3" height="26" fill="#3b7bd6"/></g>
      <g><rect x="26" y="38" width="3" height="32" fill="#2f2d30"/><rect x="30" y="46" width="3" height="24" fill="#f05a22"/><rect x="34" y="28" width="3" height="42" fill="#3b7bd6"/></g>
      <g><rect x="48" y="30" width="3" height="40" fill="#2f2d30"/><rect x="52" y="20" width="3" height="50" fill="#f05a22"/><rect x="56" y="38" width="3" height="32" fill="#3b7bd6"/></g>
      <g><rect x="70" y="36" width="3" height="34" fill="#2f2d30"/><rect x="74" y="24" width="3" height="46" fill="#f05a22"/><rect x="78" y="44" width="3" height="26" fill="#3b7bd6"/></g>
      <g><rect x="92" y="14" width="3" height="56" fill="#2f2d30"/><rect x="96" y="32" width="3" height="38" fill="#f05a22"/><rect x="100" y="42" width="3" height="28" fill="#3b7bd6"/></g>
      <g><rect x="114" y="26" width="3" height="44" fill="#2f2d30"/><rect x="118" y="10" width="3" height="60" fill="#f05a22"/><rect x="122" y="20" width="3" height="50" fill="#3b7bd6"/></g>
      <g font-family="Raleway,Arial,sans-serif" font-size="3" fill="#7d7c80"><rect x="42" y="76" width="2" height="2" fill="#2f2d30"/><text x="45" y="78">Sales</text><rect x="56" y="76" width="2" height="2" fill="#f05a22"/><text x="59" y="78">Market</text><rect x="72" y="76" width="2" height="2" fill="#3b7bd6"/><text x="75" y="78">Cost</text></g>
    </svg>
    <div class="abs" style="left:190px;top:124px;display:flex;align-items:center;gap:5px"><svg width="9" height="8" viewBox="0 0 10 9"><path d="M5 0 L10 9 H0Z" fill="#2f2d30"/></svg><span style="font-size:20px;font-weight:700;color:var(--blue)">85%</span></div>
    <div class="abs" style="left:204px;top:150px;font-size:4.5px;font-weight:700;color:var(--orange)">Profit</div>
    <div class="abs small" style="left:204px;top:157px;width:50px;font-size:3px">Short note about this point of the plan.</div>
  </section>

  <!-- 18 Mockup monitor -->
  <section class="slide">
    <div class="abs" style="left:0;top:0;width:343px;height:100px;background:var(--dark-2)"></div>
    <div class="abs" style="left:15px;top:13px;font-size:10px;color:#fff">OUR MOCKUP AREA</div>
    <div class="abs" style="left:15px;top:43px;width:135px">
      <div style="font-size:5.5px;color:#fff;margin-bottom:3px">Heading Here</div>
      <div class="col-text" style="color:#d9d8db">Simple tools for coaches who want clear plans and better team results.</div>
    </div>
    <div class="abs" style="left:146px;top:16px;width:180px;height:112px;background:#1f1e20;border-radius:4px;padding:6px"><div class="photo" role="img" aria-label="Photo of an athlete clapping chalk-dusted hands" style="position:relative;width:100%;height:100%;background:radial-gradient(ellipse at 50% 40%,#b8b7ba,#5a595c 45%,#1a191b 85%)"></div></div>
    <div class="abs" style="left:146px;top:128px;width:180px;height:10px;background:#dcdcde"></div>
    <div class="abs" style="left:222px;top:138px;width:28px;height:18px;background:linear-gradient(#c6c6c9,#e4e4e6)"></div>
    <div class="abs" style="left:208px;top:156px;width:56px;height:2px;background:#bdbdc0"></div>
    <div class="abs" style="left:16px;top:112px;width:120px;display:flex;flex-direction:column;gap:9px">
      <div style="display:flex;gap:6px"><span class="icon-dot" style="border:1.2px solid var(--orange);flex:none"></span><span class="small">Simple tools for coaches who want clear plans and better team results.</span></div>
      <div style="display:flex;gap:6px"><span class="icon-dot" style="background:var(--blue);flex:none"></span><span class="small">Simple tools for coaches who want clear plans and better team results.</span></div>
    </div>
    <div class="foot"><span>© Copyright 2018 Keenfield Athletics. All rights reserved.</span><span class="rule"></span><span>18</span></div>
    <div class="flag l"><i></i><i></i><i></i></div><div class="flag r"><i></i><i></i><i></i></div>
  </section>

</main>
</body>
</html>
```